KVR Biz Cards

We are a property management company that manages luxury level residential estates. As such, we need a business card design that gives a high end feel. The idea at the moment is to list the services offered on the back of the card, and our company information on the front of the card.

Services for the back of the card are as follows:
Professional Property Management service, Home Hosting & Concierge Service, Holliday Home / Income Property Management

```html
<!DOCTYPE html>
<html lang="en">
<head>
<meta charset="utf-8">
<title>KVR Business Cards</title>
<link href="https://fonts.googleapis.com/css2?family=Montserrat:wght@400;500;600&display=swap" rel="stylesheet">
<style>
  :root {
    --backdrop: #8e8e8e;
    --card: #141416;
    --ink: #f2f2f2;
    --ink-soft: #d6d6d6;
  }
  * { margin: 0; padding: 0; box-sizing: border-box; }
  html, body { width: 1200px; height: 1056px; overflow: hidden; }
  body {
    background: var(--backdrop);
    font-family: "Montserrat", Arial, sans-serif;
    color: var(--ink);
    position: relative;
  }
  .card {
    position: absolute;
    left: 230px;
    width: 740px;
    height: 424px;
    background: var(--card);
    border-radius: 4px;
    box-shadow: 0 18px 40px rgba(0,0,0,.28);
    overflow: hidden;
  }
  .card--front { top: 64px; }
  .card--back { top: 566px; }

  .frame-lines { position: absolute; inset: 0; }
  .frame-lines line { stroke: var(--ink); stroke-width: 1.6; }

  .contact {
    position: absolute;
    left: 58px;
    top: 236px;
  }
  .contact__role {
    font-size: 19px;
    font-weight: 400;
    letter-spacing: .5px;
    padding-bottom: 12px;
    padding-left: 8px;
  }
  .contact__rule {
    width: 196px;
    height: 1.6px;
    background: var(--ink);
    margin-bottom: 12px;
  }
  .contact__list { list-style: none; }
  .contact__item {
    display: flex;
    align-items: center;
    gap: 9px;
    font-size: 17px;
    line-height: 27px;
    color: var(--ink-soft);
  }
  .contact__icon {
    width: 15px; height: 15px;
    border-radius: 50%;
    background: var(--ink);
    display: flex; align-items: center; justify-content: center;
    flex: none;
  }
  .contact__icon svg { width: 9px; height: 9px; }

  .brand-mark {
    display: flex;
    align-items: center;
    gap: 10px;
    font-weight: 600;
    color: var(--ink);
    letter-spacing: 2px;
  }
  .brand-mark__square { border: 2px solid var(--ink); flex: none; }

  .card--front .brand-mark {
    position: absolute;
    right: 86px;
    top: 148px;
    font-size: 34px;
  }
  .card--front .brand-mark__square { width: 26px; height: 26px; }

  .back-content {
    position: absolute;
    inset: 0;
    display: flex;
    flex-direction: column;
    align-items: center;
    padding-top: 70px;
    text-align: center;
  }
  .card--back .brand-mark { font-size: 56px; letter-spacing: 4px; }
  .card--back .brand-mark__square { width: 40px; height: 40px; }
  .company-name {
    margin-top: 18px;
    font-size: 30px;
    font-weight: 600;
    letter-spacing: 1px;
  }
  .tagline {
    font-size: 22px;
    font-weight: 400;
    margin-top: 2px;
  }
  .tagline-rule {
    width: 196px;
    height: 1.6px;
    background: var(--ink);
    margin: 16px 0 16px;
  }
  .services {
    list-style: none;
    font-family: Arial, Helvetica, sans-serif;
    font-size: 17px;
    line-height: 26px;
    color: var(--ink);
  }
  .services__row span + span { margin-left: 14px; }
</style>
</head>
<body>

<section class="card card--front" aria-label="Business card front">
  <svg class="frame-lines" width="740" height="424" viewBox="0 0 740 424" aria-hidden="true">
    <line x1="80" y1="40" x2="80" y2="150"/>
    <line x1="80" y1="40" x2="690" y2="40"/>
    <line x1="690" y1="40" x2="690" y2="384"/>
    <line x1="330" y1="384" x2="690" y2="384"/>
  </svg>

  <div class="brand-mark">
    <span>KVR</span>
    <span class="brand-mark__square"></span>
  </div>

  <div class="contact">
    <p class="contact__role">Manager</p>
    <div class="contact__rule"></div>
    <ul class="contact__list">
      <li class="contact__item">
        <span class="contact__icon"><svg viewBox="0 0 10 10"><path d="M2 1.5l1.6-.3.8 2-1 .8a5 5 0 0 0 2.6 2.6l.8-1 2 .8-.3 1.6C6.5 8.3 1.7 3.5 2 1.5z" fill="#141416"/></svg></span>
        123-456-7899
      </li>
      <li class="contact__item">
        <span class="contact__icon"><svg viewBox="0 0 10 10"><rect x="1.5" y="2.5" width="7" height="5" fill="none" stroke="#141416" stroke-width="1"/><path d="M1.5 2.5L5 5.5l3.5-3" fill="none" stroke="#141416" stroke-width="1"/></svg></span>
        info@kestrelvale.com
      </li>
      <li class="contact__item">
        <span class="contact__icon"><svg viewBox="0 0 10 10"><circle cx="5" cy="5" r="3.4" fill="none" stroke="#141416" stroke-width="1"/><path d="M1.6 5h6.8M5 1.6c-1.6 2-1.6 4.8 0 6.8M5 1.6c1.6 2 1.6 4.8 0 6.8" fill="none" stroke="#141416" stroke-width=".8"/></svg></span>
        www.kestrelvale.com
      </li>
      <li class="contact__item">
        <span class="contact__icon"><svg viewBox="0 0 10 10"><path d="M5 9S2 5.6 2 3.8a3 3 0 0 1 6 0C8 5.6 5 9 5 9z" fill="#141416"/><circle cx="5" cy="3.8" r="1" fill="#f2f2f2"/></svg></span>
        123, Your Street Name, 12 city
      </li>
    </ul>
  </div>
</section>

<section class="card card--back" aria-label="Business card back">
  <div class="back-content">
    <div class="brand-mark">
      <span>KVR</span>
      <span class="brand-mark__square"></span>
    </div>
    <h1 class="company-name">KESTREL VALE RESIDENCES</h1>
    <p class="tagline">Engineered to Give You Peace of Mind</p>
    <div class="tagline-rule"></div>
    <ul class="services">
      <li class="services__row"><span>• Professional Property Management service</span><span>• Home Hosting &amp; Concierge Service,</span></li>
      <li class="services__row"><span>• Holliday Home / Income Property Management</span></li>
    </ul>
  </div>
</section>

</body>
</html>
```